Business Card Design Project

Hello
I want a Simple Business card that uses the company logo that is easily reasonable but looks professional as I am an IT Services company and would look to share these cards with prospective clients.
The details are:
Kestrel Arc Solutions
14 Morrow Lane
Birmingham
B7 4QX
Telephone 0845 217 6640
I would like my name Oliver Hastings and my title Director on the card.
Target Market(s)
IT Professionals
Industry/Entity Type
Business

```html
<!DOCTYPE html>
<html lang="en">
<head>
<meta charset="utf-8">
<title>Kestrel Arc Solutions – Business Card</title>
<link rel="stylesheet" href="https://fonts.googleapis.com/css2?family=Open+Sans:wght@400;600;700&display=swap">
<style>
  :root {
    --backdrop: #e8e8e5;
    --card: #ffffff;
    --ink: #2b2b2b;
    --ink-soft: #4a4a4a;
    --green: #3fb51f;
    --green-light: #8fd05a;
    --divider: #9a9a9a;
  }
  * { margin: 0; padding: 0; box-sizing: border-box; }
  html, body {
    width: 1200px;
    height: 856px;
    overflow: hidden;
    background: var(--backdrop);
    font-family: "Open Sans", Arial, sans-serif;
  }
  .business-card {
    position: absolute;
    left: 150px;
    top: 171px;
    width: 900px;
    height: 514px;
    background: var(--card);
    box-shadow: 0 6px 24px rgba(0,0,0,0.12);
    overflow: hidden;
  }
  .card-edge {
    position: absolute;
    left: 0; right: 0; bottom: 0;
    height: 12px;
    background: var(--green);
  }
  .brand {
    position: absolute;
    left: 120px;
    top: 130px;
    display: flex;
    align-items: center;
    gap: 14px;
  }
  .brand-dot {
    width: 38px;
    height: 38px;
    border-radius: 50%;
    background: var(--green-light);
  }
  .brand-name {
    font-size: 34px;
    font-weight: 700;
    color: var(--ink);
    letter-spacing: -0.5px;
  }
  .divider {
    position: absolute;
    left: 500px;
    top: 205px;
    width: 2px;
    height: 120px;
    background: linear-gradient(to bottom, rgba(154,154,154,0.2), var(--divider));
  }
  .person {
    position: absolute;
    right: 430px;
    top: 268px;
    text-align: right;
  }
  .person-name {
    font-size: 36px;
    font-weight: 400;
    color: var(--ink-soft);
    line-height: 1.15;
  }
  .person-title {
    font-size: 26px;
    font-weight: 400;
    color: var(--green);
    line-height: 1.2;
  }
  .contact {
    position: absolute;
    left: 540px;
    top: 160px;
    font-size: 22px;
    color: var(--ink);
    line-height: 1.3;
  }
  .contact-row {
    display: flex;
    align-items: flex-start;
    gap: 14px;
    margin-bottom: 22px;
  }
  .contact-icon {
    width: 20px;
    height: 24px;
    flex: none;
    margin-top: 3px;
  }
</style>
</head>
<body>
  <main class="business-card">
    <div class="brand">
      <span class="brand-dot"></span>
      <span class="brand-name">Kestrel Arc Solutions</span>
    </div>

    <div class="divider"></div>

    <div class="person">
      <p class="person-name">Oliver Hastings</p>
      <p class="person-title">Director</p>
    </div>

    <div class="contact">
      <div class="contact-row">
        <svg class="contact-icon" viewBox="0 0 20 24" aria-hidden="true">
          <path d="M10 0C4.8 0 1 3.9 1 9c0 6.5 9 15 9 15s9-8.5 9-15c0-5.1-3.8-9-9-9z" fill="var(--green)"/>
          <circle cx="10" cy="9" r="3.4" fill="#fff"/>
        </svg>
        <address style="font-style:normal">14 Morrow Lane<br>Birmingham, B7 4QX</address>
      </div>
      <div class="contact-row">
        <svg class="contact-icon" viewBox="0 0 24 24" aria-hidden="true">
          <path d="M6.6 10.8c1.4 2.8 3.8 5.1 6.6 6.6l2.2-2.2c.3-.3.7-.4 1-.2 1.1.4 2.3.6 3.6.6.6 0 1 .4 1 1V20c0 .6-.4 1-1 1C10.6 21 3 13.4 3 4c0-.6.4-1 1-1h3.5c.6 0 1 .4 1 1 0 1.3.2 2.5.6 3.6.1.3 0 .7-.2 1z" fill="var(--green)"/>
        </svg>
        <span>0845 217 6640</span>
      </div>
    </div>

    <div class="card-edge"></div>
  </main>
</body>
</html>
```